Web Design with a Twist! Not cheap design

Please note that this project is ending at 5pm on Tuesday the 28th of September, Australian Western Standard Time!!

Please also note that this project has now been guaranteed!

This project involves three primary elements:
* Logo design;
* Web design - of additional pages and page elements to fit into a site that is already in design/development;
* Graphic design - various images used on the site.

The following materials are included for the project:
* Project requirements
* Company / Site name
* Company / Site description
* Wireframes for new pages / page elements
* Screenshots of existing designs and accompanying definition of constraints for new designs
* PSDs for existing site designs
* Technical requirements for designs
* Content (to guide designs)

Project Requirements:

* Logo design:
This is a new company / site, so we need a new logo. We want to see what you come up with here without giving too much direction that may restrict creativity. If desired, you may find possible guidance through considering the company name, company description, and the existing site designs. Please note that the current logo in the site is for placeholder purposes only.

* Web design:
We need the following pages (and features) to be designed for the site:
• Home page
• Advertise page
• How it works page
We’ve provided some wireframes for the pages, however we definitely don't want you to be guided by the layout/styling at all - the wireframes are only there to indicate the features that we require on each page only. So please ignore all aspects of the wireframes except for the indications of features and functionality.

* Graphic design:
We need various images to be designed throughout the site. These include:
• The image at the top of the ‘Home’ page – please note we will provide some direction on this asap
• The image at the top of the ‘Advertise’ page – please note we will provide some direction n this asap
• The image at the top of the ‘How it Works’ pages
• The images that accompany each of the left hand menu items on the ‘How it Works’ pages (the main images & thumbnails if that’s part of your design). Please note that these images need to be constructed to match the Headlines for each of the ‘What’, ‘Who’, ‘Where’, etc menu items. These Headlines (and some descriptive text) can be found in the Content section at the end of this brief.
• The map of Australia for the ‘Home’ page
• The images to accompany the pricing section of the ‘Advertise’ page
• The variations of the ‘Days on the finder road’ images that are used on the ‘Home’, ‘Advertise’, and ‘How it Works’ pages. Please note that if you want to use different imagery (or no imagery, dependent upon your design) for the Home and Advertise pages then this is your call.

Company Name:
WorkLoom

Company / Site description:
This site will provide a means for contractors ('advertisers') to easily specify and advertise their services, coupled with a means for employers (‘buyers’) to easily seek out and contact these people.
The site will cater for contractor-side advertisements only; job postings will not be accommodated (turning the traditional job advertisement model on its head).
In general, the functionality of the site is somewhat like a mashup of sites like tallowmesh.com and brindlequay.com. The site will incorporate the following primary features of contractor profile display and search, company profile display, (and an availability calendar for v2 release).

Constraints for designs:
On some of the existing designs you will notice that a number of the elements of the site have already been designed. When constructing your designs, please work in accordance with the following constraints:

You have to keep:
• Colour scheme in the header
• Colour scheme in the top navigation buttons (including text colour and background colour)
• Colour scheme for the buttons like on the Register page

You can ignore:
• The existing placeholder logo
• Border, layout, and colour scheme for page elements (like the lines around and inside the register section on the Register page)
• Design of text fields
• Font colour scheme throughout the site – the orange and grey headlines and body text
• Design and colour scheme of the map of Australia
• The breadcrumbs (whether or not they appear, and their layout, styling, colour scheme etc)
• Dropdown styling (assuming you had to make some; currently not on any pages we’re asking you to do) like on the Browse Profession page
• Profile styling (for the home page featured profiles) like on the Browse Profession page
• Footer styling
• Anything else we haven’t explicitly asked you to keep

Technical requirements for design:
Any site designs in either Layered Photoshop files (PSD's) or Illustrator Drawings (AI). RGB Color. Must fit current site design, we work to 1024 wide screens. Usuable area is defined in site designs that are attached in the Photoshop documents; it's around 960px.
Logo work needs to be Illustrator Drawings (AI) and EPS. Need CMYK images for printing and RGB for screen. Logos must include any special fonts that are used as TTF or Open Type. Logos need Color, Monochrome, Reversed and both Tall and Wide usages.

Content for the 'How it Works' pages - this content should guide the images that appear on each page.
* What
Headline: WorkLoom brings contractors and employers together
Descriptive text: (turns the traditional job search model on its head)
* Who
Headline: WorkLoom is for highly skilled professionals and fast moving companies
Descriptive text:
* Where
Headline: Anywhere in Australia, WorkLoom is working by your side
Descriptive text:
* Why
Headline: There are more than 1 million reasons to love WorkLoom
Descriptive text: In Australia, there are 1 million people who work as contractors in their main job, and a further 100,000 people who are contractors in their second job. That’s a lot of contractors!
* When
Headline: WorkLoom is forming partnerships 24 hours a day
Descriptive text:
* How
Headline: Days on the finder road, with WorkLoom
Descriptive text: Advertise on WorkLoom now, and get your days on the finder road.

Remember
Just remember the wireframes we have submitted are just a guide – we want to see your creativity shine. And above all else - have fun!
Thank you.

Please note the deadline for this design competition 5pm on Tuesday the 28th of September, Australian Western Standard Time.

Just under 3 days away!

The deadline of the project will soon be updated to reflect this.

Hi Designers!

Just to be 100% clear about the deadline - the timer is currently showing 7 hours too many. In other words, the project will end 7 hours before the timer finishes.

I will send a notification if the timer starts to display the correct time. So until then, please remember that the deadline is earlier than it seems!

Thanks

Hi Designers,

A couple of really important points:

Firstly - if everyone could please stick to the theme that we provided in the Photoshop files that would be excellent. It is not possible for us to create a new theme. We're dealing with very tight deadlines, so please just provide designs that fit within the current theme.

Secondly, we were really hoping for more illustrations / graphics to be provided in the designs. We're not a fan of the stock photos of generic business people. So please send through designs that incorporate illustrations / graphics for any imagery.

Also just a reminder that this competition is still ending 7 hours earlier than the timer currently displays.

Thanks.

Target Market(s)

The ‘advertiser’ target market for the site is white collar professionals, in all types of industries. The site will be catering for premium contractors only. The site will be catering for both 'in person' contractors, as well as 'knowledge economy' contractors. The site will not be seeking to compete with quorvane.com, pelbix.com, marnoft.com, or similar sites.

The advertiser target market will also encompass companies and labour hire agencies that have contractors in their workforce.

The ‘buyer’ target market will encompass employers, recruitment agents, and member-to-member hiring.

Requirements
Must have
• As per overview
Nice to have
• As per overview
Should not have
• As per overview

```html
<!DOCTYPE html>
<html lang="en">
<head>
<meta charset="utf-8">
<title>WorkLoom – Home Page Design</title>
<link rel="stylesheet" href="https://fonts.googleapis.com/css2?family=Arimo:wght@400;700&display=swap">
<style>
  :root {
    --orange: #fa5b00;
    --orange-light: #ff8a3d;
    --orange-pale: #fcc29a;
    --slate: #627080;
    --slate-dark: #4f5b69;
    --tab: #b3bac3;
    --tab-text: #5c6774;
    --panel-top: #ececec;
    --panel-bottom: #cfcfcf;
    --footer: #e3e3e3;
    --text: #3d3d3d;
    --white: #ffffff;
  }
  * { box-sizing: border-box; margin: 0; padding: 0; }
  html, body { width: 837px; height: 1200px; overflow: hidden; }
  body {
    position: relative;
    background: var(--white);
    font-family: "Arimo", Arial, sans-serif;
    color: var(--text);
  }
  .abs { position: absolute; }

  /* Brand mark */
  .brand-mark {
    position: absolute; left: 0; top: 14px; width: 837px;
    text-align: center; font-weight: 700; font-size: 132px;
    letter-spacing: -4px; color: var(--slate); line-height: 1;
  }

  /* Presentation board */
  .board { position: absolute; left: 0; top: 186px; width: 837px; height: 1014px; background: var(--orange); }

  .page { position: absolute; left: 42px; top: 232px; width: 753px; height: 923px; background: var(--white); }
  .site-header { position: absolute; left: 0; top: 0; width: 753px; height: 80px; background: var(--slate); }
  .header-logo {
    position: absolute; left: 46px; top: 13px; width: 140px; height: 57px;
    background: var(--orange); border-radius: 9px;
    color: var(--white); font-weight: 700; font-size: 25px;
    display: flex; align-items: center; justify-content: center; letter-spacing: -0.5px;
  }
  .search-field { position: absolute; left: 570px; top: 14px; width: 138px; height: 15px; background: var(--white); border: 1px solid #d5d5d5; }
  .search-field svg { position: absolute; left: 3px; top: 2px; }
  .search-go {
    position: absolute; left: 712px; top: 14px; width: 23px; height: 15px;
    background: #a6adb6; color: var(--white); font-size: 8px; font-weight: 700;
    display: flex; align-items: center; justify-content: center;
  }
  .main-nav { position: absolute; left: 230px; top: 60px; display: flex; gap: 6px; }
  .main-nav a {
    width: 68px; height: 20px; background: var(--tab); color: var(--tab-text);
    font-size: 10px; font-weight: 700; text-decoration: none;
    display: flex; align-items: center; justify-content: center;
    border-radius: 3px 3px 0 0;
  }
  .main-nav a.is-current { background: var(--white); color: var(--slate-dark); }

  .content-area {
    position: absolute; left: 23px; top: 80px; width: 707px; height: 756px;
    background: linear-gradient(var(--panel-top), var(--panel-bottom));
  }
  .site-footer { position: absolute; left: 23px; top: 836px; width: 707px; height: 87px; background: var(--footer); }

  /* Hero */
  .hero {
    position: absolute; left: 128px; top: 328px; width: 589px; height: 171px;
    border: 2px solid #8d9299; border-radius: 8px; overflow: hidden;
    background: linear-gradient(175deg, #fff4ec 0%, #fbd2b4 40%, var(--orange-light) 62%, var(--orange) 100%);
  }
  .hero-name {
    position: absolute; right: 28px; bottom: 12px;
    color: var(--white); font-weight: 700; font-size: 44px; letter-spacing: -1px;
  }

  /* Area search */
  .area-search { position: absolute; left: 130px; top: 507px; width: 585px; height: 165px; background: var(--white); border-radius: 7px; overflow: hidden; }
  .area-search .swoosh { position: absolute; left: 0; top: 0; }
  .area-map { position: absolute; left: 19px; top: 6px; width: 168px; height: 155px; background: var(--orange); border-radius: 30px 40px 20px 50px; }
  .area-title { position: absolute; left: 290px; top: 30px; width: 265px; text-align: center; color: var(--white); font-weight: 700; font-size: 13px; }
  .keyword-field {
    position: absolute; left: 291px; top: 61px; width: 263px; height: 17px;
    background: var(--white); font-size: 9.5px; font-weight: 700; color: #333;
    display: flex; align-items: center; justify-content: center;
  }
  .area-button {
    position: absolute; left: 313px; top: 96px; width: 220px; height: 45px;
    background: linear-gradient(#ff8c2a, #f26100); border: 1px solid #6a3510; border-radius: 6px;
    color: var(--white); font-size: 11.5px; font-weight: 700;
    display: flex; align-items: center; justify-content: center;
  }

  /* Cards */
  .card { position: absolute; background: var(--white); border-radius: 7px; overflow: hidden; }
  .card-title {
    position: absolute; left: 0; top: 15px; width: 100%; height: 17px;
    background: var(--orange); color: var(--white); font-size: 10px; font-weight: 700;
    padding-left: 9px; display: flex; align-items: center;
  }
  .intro-card { left: 131px; top: 694px; width: 269px; height: 223px; }
  .intro-copy { position: absolute; left: 32px; top: 48px; width: 210px; font-size: 8.6px; line-height: 1.25; }
  .intro-copy p + p { margin-top: 10px; }

  .register-card { left: 131px; top: 932px; width: 269px; height: 110px; }
  .register-badge {
    position: absolute; left: 12px; top: 9px; width: 86px; height: 86px; border-radius: 50%;
    background: var(--orange); color: var(--white); text-align: center;
    display: flex; flex-direction: column; align-items: center; justify-content: center;
    font-weight: 700; line-height: 1.05;
  }
  .register-badge .badge-main { font-size: 14px; }
  .register-badge .badge-sub { font-size: 8px; margin-top: 2px; }
  .register-copy { position: absolute; left: 116px; top: 14px; width: 145px; font-size: 8.6px; line-height: 1.25; }

  .featured-card { left: 413px; top: 694px; width: 304px; height: 348px; }
  .profile-photo { position: absolute; left: 31px; width: 105px; height: 74px; background: var(--slate); border-radius: 12px; }
  .profile-region { position: absolute; left: 173px; width: 85px; height: 74px; background: var(--orange); border-radius: 18px 24px 14px 26px; }
  .more-button {
    position: absolute; left: 108px; top: 314px; width: 109px; height: 22px;
    background: var(--orange); border-radius: 3px; color: var(--white); font-size: 8.5px;
    display: flex; align-items: center; justify-content: center;
  }

  /* Footer links */
  .footer-col { position: absolute; top: 1082px; font-size: 8.8px; color: #7a7f86; line-height: 1.2; }
  .footer-col h4 { font-size: 12px; color: var(--slate); font-weight: 700; margin-bottom: 1px; }
  .copyright { position: absolute; left: 539px; top: 1082px; font-size: 12px; font-weight: 700; color: var(--slate); }
</style>
</head>
<body>

  <div class="brand-mark">WorkLoom</div>

  <div class="board"></div>

  <div class="page">
    <header class="site-header">
      <div class="header-logo">WorkLoom</div>
      <div class="search-field">
        <svg width="10" height="10" viewBox="0 0 10 10"><circle cx="4" cy="4" r="2.8" fill="none" stroke="#f07a1a" stroke-width="1.4"/><line x1="6" y1="6" x2="9" y2="9" stroke="#f07a1a" stroke-width="1.6"/></svg>
      </div>
      <div class="search-go">Go</div>
      <nav class="main-nav">
        <a class="is-current">Home</a>
        <a>Find</a>
        <a>Advertise</a>
        <a>How it Works</a>
        <a>Blog</a>
        <a>Login</a>
      </nav>
    </header>
    <div class="content-area"></div>
    <footer class="site-footer"></footer>
  </div>

  <section class="hero" role="img" aria-label="Banner scene of business people meeting and shaking hands on an orange backdrop">
    <div class="hero-name">WorkLoom</div>
  </section>

  <section class="area-search">
    <svg class="swoosh" width="585" height="165" viewBox="0 0 585 165">
      <path d="M300 0 H585 V165 H215 C222 90 250 25 300 0 Z" fill="var(--orange)"/>
      <path d="M330 165 C350 110 420 60 585 40 V75 C460 90 390 125 370 165 Z" fill="var(--orange-light)" opacity="0.7"/>
    </svg>
    <div class="area-map" role="img" aria-label="Map of Australia with selectable states"></div>
    <h2 class="area-title">Find Highly Skilled Professionals</h2>
    <div class="keyword-field">[Search for Keyword]</div>
    <div class="area-button">Find Contractors in this Area</div>
  </section>

  <section class="card intro-card">
    <h3 class="card-title">Lorem Ipsum Dolor</h3>
    <div class="intro-copy">
      <p>sit amet, consetetur sadipscing elitr, sed diam nonumy eirmod te.</p>
      <p>mpor invidunt ut labore et dolore magna aliquyam erat, sed diam voluptua. At vero eos et accusam et justo duo dolores et ea rebum. Stet clita kasd gubergren, no sea takimata sanctus est Lorem ipsum dolor sit amet. Lorem ipsum dolor sit amet,</p>
      <p>consetetur sadipscing elitr, &nbsp;sed diam nonumy eirmod tempor invidunt ut labore et dolore magna aliquyam erat, sed diam voluptua. At vero eos et accusam et justo duo dolores et ea rebum. Stet clita kasd gubergren, no sea takimata sanctus est Lorem ipsum dolor sit amet. Lorem ipsum dolor sit amet.</p>
    </div>
  </section>

  <section class="card register-card">
    <div class="register-badge">
      <span class="badge-main">Register<br>Now!</span>
      <span class="badge-sub">Heres How...</span>
    </div>
    <p class="register-copy">mpor invidunt ut labore et dolore magna aliquyam erat, sed diam voluptua. At vero eos et accusam et justo duo dolores et ea rebum. Stet clita kasd gubergren, no sea takimata sanctus est Lorem ipsum dolor sit amet. Lorem ipsum dolor sit amet,</p>
  </section>

  <section class="card featured-card">
    <h3 class="card-title">Featured Profiles</h3>
    <div class="profile-photo" style="top:55px" role="img" aria-label="Profile photo placeholder"></div>
    <div class="profile-region" style="top:55px" role="img" aria-label="Map of Australia showing the contractor's state"></div>
    <div class="profile-photo" style="top:143px" role="img" aria-label="Profile photo placeholder"></div>
    <div class="profile-region" style="top:143px" role="img" aria-label="Map of Australia showing the contractor's state"></div>
    <div class="profile-photo" style="top:231px" role="img" aria-label="Profile photo placeholder"></div>
    <div class="profile-region" style="top:231px" role="img" aria-label="Map of Australia showing the contractor's state"></div>
    <div class="more-button">Find Other Contractors</div>
  </section>

  <div class="footer-col" style="left:155px"><h4>The Service</h4>About<br>Browse<br>Log In</div>
  <div class="footer-col" style="left:266px"><h4>Support</h4>Contact Us<br>FAQ</div>
  <div class="footer-col" style="left:353px"><h4>Legal</h4>Privacy Policy<br>Terms &amp; Conditions</div>
  <div class="copyright">© 2010 WorkLoom Pty Ltd</div>

</body>
</html>
```